Civil Engineering Business Card Design

We need a business card design for an Civil Engineering Company located in Naples, Florida. The company name is Dorvel Engineering.
What we do:
Site Evaluation
Review existing site conditions and zoning
Evaluation of potential development options
Evaluation of environmental permitting challenges
Prepare alternative master site development or redevelopment plan
Calculate cost and time lines for site development
Address political, environmental, social, and economic impacts of site development
Site Design
Prepare master site development plans
Zoning, rezoning, and zoning amendments for land use changes
Evaluate zoning and environmental permitting challenges
Value engineer alternative land development design and products
Residential Development
Plat development and design
Homeowner association document development
Single family development ranging from affordable housing to large estate projects
Multi family development ranging from duplexes to large scale condominiums
Amenity facilities such as golf courses, parks and clubhouse sites
Commercial Development
Office site and park designs development plans
Industrial site and park development plans
Shopping center site development design
Hospital site design development
Institutional Development
School design development and redevelopment plans
Park design development and enhancement plans
Downtown redevelopment plans for new and existing structures
Theater and park plan development
Parking garage design development
Governmental administration building design
Design Services
Site development
Environmental assessment
Roadway alignment and development
Surface water management
Drainage design
Water distribution system
Fire service analysis
Sewage collection systems
Sewage pump station and force main design
Cable utility conduit layout
Construction details
Construction documents
Technical specifications
Alternative methods and materials analysis
Services During Construction
Development of bid documents
Solicitation and processing of bids
Cost review and analysis
Construction cost estimating
Onsite construction observation
Coordination of field modifications to address unforeseen site conditions
Assess value engineering design and contract work
Review of pay requests and shop drawings
Review of warranties
Development assessment of onsite and offsite mitigation
Verification of construction completion, close out, and certification
Processing final pay requests and turn over
We want a clean design on a white background. We have a current logo but are not happy with it so changes would be greatly appreciated.
Industry/Entity Type
Construction
Contact Information for Business Card
Dorvel Engineering
Creative Engineering Solutions Through Integrity and Experience
Marcus Dorvel, President
4817 Bracken Loop West
Suite 418C
Naples, FL 34987
239-555-0143-Office, 239-555-0178-Mobile
Marc@DorvelEng.com, www.DorvelEng.com

```html
<!DOCTYPE html>
<html lang="en">
<head>
<meta charset="utf-8">
<title>Dorvel Engineering – Business Card</title>
<link rel="stylesheet" href="https://fonts.googleapis.com/css2?family=Exo+2:wght@400;500;700&display=swap">
<style>
  :root {
    --bg: #e6e6e6;
    --card-dark: #262626;
    --card-light: #ffffff;
    --amber: #fbb12b;
    --amber-deep: #f7a11f;
    --ink: #262626;
    --ink-soft: #444444;
    --rule: #bdbdbd;
  }
  * { margin: 0; padding: 0; box-sizing: border-box; }
  html, body { width: 1200px; height: 949px; overflow: hidden; }
  body {
    background: var(--bg);
    font-family: "Exo 2", "Segoe UI", sans-serif;
    color: var(--ink);
    position: relative;
  }
  .card {
    position: absolute;
    left: 280px;
    width: 640px;
    height: 366px;
    border-radius: 22px;
    overflow: hidden;
  }
  .card--front { top: 78px; background: var(--card-dark); }
  .card--back  { top: 504px; background: var(--card-light); box-shadow: 0 1px 0 rgba(0,0,0,.06); }

  /* front */
  .brand {
    position: absolute;
    inset: 0;
    display: flex; align-items: center; justify-content: center; gap: 22px;
  }
  .brand__mark { width: 74px; height: 74px; border-radius: 50%; background: var(--amber); }
  .brand__name { font-weight: 700; font-size: 44px; line-height: 1; color: var(--amber); letter-spacing: .5px; }

  /* back */
  .back__band { position: absolute; inset: 0; }
  .icon { position: absolute; }
  .person { position: absolute; left: 44px; top: 62px; }
  .person__name { font-size: 22px; font-weight: 500; letter-spacing: 1px; color: var(--ink); line-height: 1.2; }
  .person__role {
    font-size: 10px; font-weight: 500; letter-spacing: .8px; text-transform: uppercase;
    color: var(--ink-soft); border-top: 1px solid var(--rule); margin-top: 3px; padding-top: 3px;
    width: 170px;
  }
  .text { position: absolute; font-size: 15px; font-weight: 500; letter-spacing: .5px; color: var(--ink); line-height: 1.4; }
  .web { left: 44px; top: 212px; }
  .address { left: 270px; top: 128px; }
  .phones { right: 24px; top: 172px; text-align: right; font-size: 14px; }
  .phones__label { font-size: 11px; text-transform: uppercase; letter-spacing: .8px; color: var(--ink-soft); margin-right: 4px; }
  .social { position: absolute; left: 270px; top: 244px; list-style: none; }
  .social li { display: flex; align-items: center; gap: 12px; height: 40px; font-size: 15px; font-weight: 500; letter-spacing: .5px; }
  .social__dot { width: 28px; height: 28px; border-radius: 50%; background: var(--card-dark); flex: none; }
</style>
</head>
<body>

<section class="card card--front" aria-label="Card front">
  <div class="brand">
    <span class="brand__mark"></span>
    <span class="brand__name">Dorvel Engineering</span>
  </div>
</section>

<section class="card card--back" aria-label="Card back">
  <svg class="back__band" width="640" height="366" viewBox="0 0 640 366" aria-hidden="true">
    <defs>
      <linearGradient id="amberFill" x1="0" y1="0" x2="1" y2="1">
        <stop offset="0" stop-color="#fbb12b"/>
        <stop offset="1" stop-color="#f7a11f"/>
      </linearGradient>
    </defs>
    <polygon points="0,118 460,118 460,236 640,236 640,366 0,366" fill="url(#amberFill)"/>
  </svg>

  <svg class="icon" style="left:84px;top:18px" width="36" height="36" viewBox="0 0 36 36" aria-hidden="true">
    <circle cx="18" cy="18" r="17" fill="#fbb12b"/>
    <circle cx="18" cy="14" r="5" fill="#fff"/>
    <path d="M9 27c1-5 5-7 9-7s8 2 9 7z" fill="#fff"/>
  </svg>
  <div class="person">
    <div class="person__name">MARCUS DORVEL</div>
    <div class="person__role">President</div>
  </div>

  <svg class="icon" style="left:100px;top:146px" width="54" height="54" viewBox="0 0 54 54" aria-hidden="true">
    <circle cx="27" cy="27" r="26" fill="#262626"/>
    <rect x="14" y="16" width="26" height="17" rx="1.5" fill="none" stroke="#fff" stroke-width="2.5"/>
    <rect x="22" y="36" width="10" height="2.5" fill="#fff"/>
  </svg>
  <div class="text web">Marc@DorvelEng.com<br>www.DorvelEng.com</div>

  <svg class="icon" style="left:340px;top:74px" width="36" height="36" viewBox="0 0 36 36" aria-hidden="true">
    <circle cx="18" cy="18" r="17" fill="#fbb12b"/>
    <path d="M18 8a6.5 6.5 0 0 0-6.5 6.5C11.5 19 18 27 18 27s6.5-8 6.5-12.5A6.5 6.5 0 0 0 18 8z" fill="#fff"/>
    <circle cx="18" cy="14.5" r="2.4" fill="#fbb12b"/>
  </svg>
  <div class="text address">4817 Bracken Loop West<br>Suite 418C<br>Naples, FL 34987</div>

  <svg class="icon" style="left:578px;top:128px" width="36" height="36" viewBox="0 0 36 36" aria-hidden="true">
    <circle cx="18" cy="18" r="17" fill="#fbb12b"/>
    <rect x="13" y="8" width="10" height="19" rx="2" fill="none" stroke="#fff" stroke-width="2"/>
    <circle cx="18" cy="23.5" r="1.2" fill="#fff"/>
  </svg>
  <div class="text phones">
    <span class="phones__label">Office</span>239-555-0143<br>
    <span class="phones__label">Mobile</span>239-555-0178
  </div>

  <ul class="social">
    <li><span class="social__dot"></span>Chatterly.com/123</li>
    <li><span class="social__dot"></span>Chirpnet.com/123</li>
    <li><span class="social__dot"></span>workfolio.com/in/123</li>
  </ul>
</section>

</body>
</html>
```